IT Company looking to market towards Dental Offices

I am looking for a full-color design. Using my existing logo. Must have High Res stock photos. The brochure needs to be full page edge to edge design single fold pamphlet style. Content provided. Please see the website in attached Word Doc for more content.

```html
<!DOCTYPE html>
<html lang="en">
<head>
<meta charset="utf-8">
<title>Byte Harbor – Dental IT Brochure</title>
<link href="https://fonts.googleapis.com/css2?family=Open+Sans:ital,wght@0,300;0,400;0,600;0,700;0,800;1,400;1,700&display=swap" rel="stylesheet">
<style>
  :root{
    --navy:#0f1f6b;
    --navy-mid:#2b3f8f;
    --navy-soft:#4a5ea6;
    --sky:#2f8fd8;
    --paper:#ffffff;
    --mist:#e9ebef;
    --stage:#2e2e2e;
    --photo-chair:#8a8d91;
    --photo-rack:#2a2d33;
  }
  *{box-sizing:border-box;margin:0;padding:0}
  html,body{width:1200px;height:833px;overflow:hidden;background:var(--stage)}
  body{font-family:"Open Sans",Arial,sans-serif;position:relative}
  .spread{position:absolute;left:40px;top:20px;width:1120px;height:793px;display:flex}
  .page{position:relative;width:560px;height:793px;overflow:hidden}
  .page svg.bg{position:absolute;inset:0;width:100%;height:100%}
  .heading{position:absolute;color:#fff;font-size:30px;letter-spacing:.5px;line-height:1}
  .heading .thin{font-weight:300}
  .heading .bold{font-weight:800;font-style:italic}
  .heading::after{content:"";display:block;width:34px;height:4px;background:#fff;margin-top:6px;border-radius:2px}
  .about{left:60px;top:58px}
  .about-text{position:absolute;left:60px;top:110px;width:430px;color:#fff;font-size:10.5px;font-style:italic;line-height:1.45;text-align:justify}
  .services{left:60px;top:250px}
  .list{position:absolute;list-style:none;color:#fff;font-size:11px;font-style:italic;line-height:1.55}
  .list li::before{content:"✓";margin-right:6px;font-style:normal}
  .list .cat{font-weight:700;text-transform:uppercase;font-size:10.5px}
  .list-hw{left:60px;top:305px}
  .list-infra{left:300px;top:370px}
  .solutions{position:absolute;left:60px;top:60px;color:var(--navy);font-size:28px;font-weight:800;letter-spacing:.5px}
  .solutions::after{content:"";display:block;width:34px;height:4px;background:var(--sky);margin-top:4px;border-radius:2px}
  .list-solutions{left:60px;top:112px;color:var(--navy);font-size:11.5px}
  .list-solutions li::before{color:var(--sky)}
  .cta{position:absolute;left:50px;top:470px;color:#fff;font-size:25px;font-weight:800;font-style:italic;line-height:1.1;text-transform:uppercase}
  .cta::after{content:"";display:block;width:34px;height:4px;background:var(--sky);margin-top:8px;border-radius:2px}
  .cta-sub{position:absolute;left:50px;top:575px;color:#fff;font-size:11px;font-weight:700;font-style:italic}
  .list-steps{left:50px;top:598px;font-size:11px}
  .list-steps li::before{color:var(--sky)}
  .closing{position:absolute;left:50px;top:670px;width:470px;color:#fff;font-size:12.5px;line-height:1.4}
  .closing p+p{margin-top:6px}
</style>
</head>
<body>
<main class="spread">
  <section class="page page-left">
    <svg class="bg" viewBox="0 0 560 793" preserveAspectRatio="none">
      <defs>
        <linearGradient id="leftNavy" x1="0" y1="0" x2="1" y2="0.4">
          <stop offset="0" stop-color="#0f1f6b"/>
          <stop offset="0.65" stop-color="#1a2c7a"/>
          <stop offset="1" stop-color="#4a5ea6"/>
        </linearGradient>
        <linearGradient id="chairTone" x1="0" y1="0" x2="1" y2="1">
          <stop offset="0" stop-color="#b9bcc0"/>
          <stop offset="1" stop-color="#6e7175"/>
        </linearGradient>
      </defs>
      <rect width="560" height="793" fill="url(#leftNavy)"/>
      <path d="M420 0 C500 40 545 110 560 190 L560 0 Z" fill="var(--sky)"/>
      <path d="M0 520 L160 540 C300 520 450 540 560 600 L560 793 L0 793 Z" fill="url(#chairTone)" role="img" aria-label="Photo of a modern dental treatment room with patient chair"/>
      <path d="M300 793 C420 760 520 720 560 690 L560 793 Z" fill="var(--sky)"/>
      <path d="M420 793 C480 770 530 745 560 730 L560 793 Z" fill="var(--navy)"/>
    </svg>
    <h2 class="heading about"><span class="thin">ABOUT </span><span class="bold">US</span></h2>
    <p class="about-text">Byte Harbor offers a proven expertise in Dental Practices. We have trained engineers that specialize in Dental practice management solutions. We can handle supporting your Practice Management Software to installing IOCs, Remote &amp; Sensors, Pano's, X-rays, scanners, pen pads, and more. Being familiar with Digital technology and how your practice runs we are able to predict and plan for your growth by providing the correct configurations the first time and implementing the proper storage solutions you will require. We know Dental!</p>
    <h2 class="heading services"><span class="thin">OUR </span><span class="bold">SERVICES</span></h2>
    <ul class="list list-hw">
      <li class="cat">Hardware Sales</li>
      <li>Servers</li>
      <li>Workstations</li>
      <li>Firewalls</li>
      <li>Routers</li>
      <li>Switches</li>
      <li>TVs &amp; Monitors</li>
      <li>Wireless Equipment</li>
      <li>Custom Check-in Workstations</li>
    </ul>
    <ul class="list list-infra">
      <li class="cat">Infrastructure</li>
      <li>Data &amp; Voice Cable</li>
      <li>HDMI &amp; COAX Video Cable</li>
      <li>TV &amp; Dual Monitor Installation</li>
      <li>Mounting Hardware</li>
      <li>Wireless Installation</li>
      <li>Office Sound Solutions</li>
      <li>Custom Dental Cable</li>
      <li>Video Surveillance</li>
    </ul>
  </section>

  <section class="page page-right">
    <svg class="bg" viewBox="0 0 560 793" preserveAspectRatio="none">
      <defs>
        <linearGradient id="paperTone" x1="0" y1="0" x2="1" y2="1">
          <stop offset="0" stop-color="#f4f5f7"/>
          <stop offset="1" stop-color="#dfe2e7"/>
        </linearGradient>
        <linearGradient id="rightNavy" x1="0" y1="0" x2="1" y2="0.3">
          <stop offset="0" stop-color="#0f1f6b"/>
          <stop offset="0.55" stop-color="#3a4e9a"/>
          <stop offset="1" stop-color="#0f1f6b"/>
        </linearGradient>
        <linearGradient id="rackTone" x1="0" y1="0" x2="1" y2="1">
          <stop offset="0" stop-color="#55585e"/>
          <stop offset="1" stop-color="#1c1e22"/>
        </linearGradient>
      </defs>
      <rect width="560" height="793" fill="url(#paperTone)"/>
      <path d="M0 400 C80 380 160 400 240 420 L560 330 L560 793 L0 793 Z" fill="url(#rightNavy)"/>
      <path d="M240 420 L560 330 L560 690 C470 610 380 520 240 420 Z" fill="url(#rackTone)" role="img" aria-label="Photo of server racks in a data room"/>
      <path d="M0 650 C80 720 160 770 220 793 L0 793 Z" fill="var(--sky)"/>
    </svg>
    <h2 class="solutions">SOLUTIONS</h2>
    <ul class="list list-solutions">
      <li>Flat Rate Monthly Support</li>
      <li>Secure Backups with our ChairVault.net</li>
      <li>Secure Encrypted Emails &amp; X-Rays</li>
      <li>Practice Management Software Experts</li>
      <li>HIPAA Compliance</li>
      <li>Anti-Virus, Anti-Malware and Cyber Security</li>
      <li>Data Recovery</li>
      <li>Cloud Office &amp; Email Suites</li>
      <li>Phone VOIP &amp; SIP Trunks</li>
    </ul>
    <h2 class="cta">Ready to make<br>your technology<br>work?</h2>
    <p class="cta-sub">How To Achieve Technology Bliss for Your Practice</p>
    <ul class="list list-steps">
      <li>Schedule a FREE Network &amp; Technology Evaluation</li>
      <li>Receive your Flat Rate Price and Technology Quote</li>
      <li>Sit back and let Byte Harbor take care of everything.</li>
    </ul>
    <div class="closing">
      <p>Don't let Technology Departments, Hardware Vendors and Practice Management vendors Point Fingers at each other.</p>
      <p>We collaborate everything and everyone for you, make one call to us and let us handle your technology.</p>
    </div>
  </section>
</main>
</body>
</html>
```